Modern Business Card

Modern professional business card with more than just logo and demographic info. Something memorable.

We are a trendy/modern chiropractic group with an emphasis on neurology, hence the minimalist-type brain logo. We want to convey that modern and technical aspect with professionalism and the elite nature of our practice environment.

```html
<!DOCTYPE html>
<html lang="en">
<head>
<meta charset="utf-8">
<title>Northline Chiropractic – Business Cards</title>
<link rel="stylesheet" href="https://fonts.googleapis.com/css2?family=Montserrat:wght@400;500;700&display=swap">
<style>
  :root {
    --backdrop: #d9cdb4;
    --card: #f2f2f3;
    --ink: #1c1c1c;
    --blue: #3f76c0;
    --black: #050505;
    --white: #ffffff;
    --muted: #444;
  }
  * { box-sizing: border-box; margin: 0; padding: 0; }
  html, body { width: 1200px; height: 960px; overflow: hidden; }
  body {
    background: var(--backdrop);
    font-family: "Montserrat", Arial, sans-serif;
    color: var(--ink);
    position: relative;
  }
  .card {
    position: absolute;
    width: 520px;
    height: 297px;
    background: var(--card);
    box-shadow: 0 10px 24px rgba(0,0,0,0.18);
    overflow: hidden;
  }
  .card--appointment { left: 90px; top: 130px; }
  .card--contact { left: 590px; top: 520px; }

  .brand {
    position: absolute;
    display: flex;
    align-items: center;
    gap: 10px;
    color: var(--ink);
  }
  .brand__mark { width: 26px; height: 26px; background: var(--blue); flex: none; }
  .brand__name {
    font-weight: 500;
    font-size: 21px;
    line-height: 1.05;
    letter-spacing: 1.5px;
    text-transform: uppercase;
  }
  .brand__name small { display: block; font-size: 13px; letter-spacing: 3px; }
  .card--appointment .brand { right: 40px; top: 34px; }
  .card--contact .brand { right: 34px; top: 38px; }

  .appointment__title {
    position: absolute; left: 34px; top: 118px;
    font-weight: 700; font-size: 15px; letter-spacing: 0.5px;
  }
  .form-row {
    position: absolute; left: 44px;
    display: flex; align-items: baseline; gap: 6px;
    font-size: 12px; color: var(--muted); width: 440px;
  }
  .form-row--name { top: 150px; }
  .form-row--time { top: 174px; }
  .form-row--days { top: 200px; gap: 0; justify-content: space-between; width: 440px; }
  .dots { flex: 1; border-bottom: 1px dotted #555; height: 1px; }
  .dots--short { flex: 0 0 150px; }
  .option { display: inline-flex; align-items: center; gap: 4px; font-size: 11px; text-transform: uppercase; }
  .box { width: 9px; height: 9px; border: 1px solid #333; display: inline-block; }

  .notice {
    position: absolute; left: 0; right: 0; bottom: 30px; height: 26px;
    background: var(--blue); color: var(--white);
    font-size: 11.5px; display: flex; align-items: center; justify-content: center;
  }

  .contact__wave { position: absolute; inset: 0; }
  .contact__details { position: absolute; left: 36px; top: 178px; color: var(--white); }
  .contact__name { color: var(--blue); font-weight: 700; font-size: 20px; }
  .contact__role { font-size: 12px; margin: 2px 0 8px 2px; }
  .contact__list { list-style: none; font-size: 11.5px; line-height: 17px; }
  .contact__list li { display: flex; align-items: center; gap: 9px; }
  .contact__list svg { width: 11px; height: 11px; flex: none; }
</style>
</head>
<body>

<section class="card card--appointment" aria-label="Appointment card">
  <div class="brand">
    <span class="brand__mark"></span>
    <span class="brand__name">Northline<small>Chiropractic</small></span>
  </div>
  <h2 class="appointment__title">APPOINTMENT</h2>
  <div class="form-row form-row--name"><span>Name:</span><span class="dots"></span></div>
  <div class="form-row form-row--time">
    <span>Time:</span><span class="dots dots--short"></span>
    <span class="option"><span class="box"></span>AM</span>
    <span class="option"><span class="box"></span>PM</span>
    <span>Date:</span><span class="dots"></span>
  </div>
  <div class="form-row form-row--days">
    <span class="option"><span class="box"></span>Mon</span>
    <span class="option"><span class="box"></span>Tues</span>
    <span class="option"><span class="box"></span>Wed</span>
    <span class="option"><span class="box"></span>Thur</span>
    <span class="option"><span class="box"></span>Fri</span>
    <span class="option"><span class="box"></span>Sat</span>
  </div>
  <p class="notice">If you are unable to keep your appointment, please call us within 24 hours.</p>
</section>

<section class="card card--contact" aria-label="Contact card">
  <svg class="contact__wave" viewBox="0 0 520 297" preserveAspectRatio="none" aria-hidden="true">
    <path d="M0,172 C120,130 260,142 380,128 C440,120 480,100 505,80" fill="none" stroke="var(--blue)" stroke-width="4"/>
    <path d="M0,180 C120,138 260,150 380,136 C440,128 480,108 520,82 L520,297 L0,297 Z" fill="var(--black)"/>
  </svg>
  <div class="brand">
    <span class="brand__mark"></span>
    <span class="brand__name">Northline<small>Chiropractic</small></span>
  </div>
  <div class="contact__details">
    <h1 class="contact__name">Daniel Marsh</h1>
    <p class="contact__role">Owner</p>
    <ul class="contact__list">
      <li><svg viewBox="0 0 12 12"><path d="M2 1 L4.5 1 L5.5 3.5 L4 4.8 C4.8 6.5 5.6 7.3 7.2 8 L8.5 6.5 L11 7.5 L11 10 C6 10.5 1.5 6 2 1 Z" fill="var(--blue)"/></svg>(555) 014-2288</li>
      <li><svg viewBox="0 0 12 12"><rect x="1" y="2.5" width="10" height="7" fill="none" stroke="var(--blue)" stroke-width="1.2"/><path d="M1 2.5 L6 7 L11 2.5" fill="none" stroke="var(--blue)" stroke-width="1.2"/></svg>info@northlinechiro.com</li>
      <li><svg viewBox="0 0 12 12"><circle cx="6" cy="6" r="5" fill="none" stroke="var(--blue)" stroke-width="1.1"/><ellipse cx="6" cy="6" rx="2.2" ry="5" fill="none" stroke="var(--blue)" stroke-width="1"/><path d="M1 6 H11" stroke="var(--blue)"/></svg>www.northlinechiro.com</li>
      <li><svg viewBox="0 0 12 12"><path d="M6 11 C3 7.5 2 6 2 4.5 A4 4 0 0 1 10 4.5 C10 6 9 7.5 6 11 Z" fill="none" stroke="var(--blue)" stroke-width="1.2"/><circle cx="6" cy="4.6" r="1.4" fill="var(--blue)"/></svg>Maple Grove Rd. Fairview, OH 45000</li>
    </ul>
  </div>
</section>

</body>
</html>
```